Spice Mix Label Bottle Branding - Health and Weight Loss Mixes

The company is called ZestoLane Spice Mix's. We've created 5 spice mixes using ingredients that promote health and weight loss. We already have a logo but now we need labels for our bottles. We would like to see designs that have the feel of health supplements (see attached examples)

We would like a different colour featured with each of our flavours.

Our flavours are:
-Golden Chai (Yellow)
-Mild Curry (Orange)
-Coffee Rub (brown)
-Garlic Oregano (Green)
-Taco (Blue)

Thank you!

Target Market(s)

Ages 22-35. Men and Female. Trendy, Hipster.

Industry/Entity Type

Food Production

Font styles to use
Sans Serif

Colors
f37122
0655a3
0692cd
9bcb3c
fbee3f

Requirements
Must have
• A different featured colour for each flavour.
• The ZestoLane Spices Logo (attached)
• The slogan: "Weight Loss Ingredients"
• -Golden Chai (Yellow)
• -Mild Curry (Orange)
• -Coffee Rub (brown)
• -Garlic Oregano (Green)
• -Taco (Blue)
• Text Files attached.
Nice to have
• A black label with a featured colour for each of the spice mice flavours.
• 'No Salt added'

```html
<!DOCTYPE html>
<html lang="en">
<head>
<meta charset="utf-8">
<title>ZestoLane Spices – Seasoning Labels</title>
<link rel="stylesheet" href="https://fonts.googleapis.com/css2?family=Montserrat:wght@700;800&display=swap">
<style>
  :root {
    --canvas: #ffffff;
    --label-cream: #f6f4ec;
    --ink: #141414;
    --curry: #dd4a0c;
    --chai: #c8921f;
    --oregano: #98b02e;
    --coffee: #9a5f32;
    --taco: #2f6394;
    --flavour-text: #fbf6ea;
  }
  * { box-sizing: border-box; margin: 0; padding: 0; }
  html, body { width: 1200px; height: 1200px; overflow: hidden; background: var(--canvas); }
  .sheet { position: relative; width: 1200px; height: 1200px; }

  .label {
    position: absolute;
    width: 209px;
    height: 284px;
    background: var(--label-cream);
    overflow: hidden;
    font-family: "Montserrat", sans-serif;
    box-shadow: 0 1px 4px rgba(0,0,0,0.12);
  }
  .label--curry   { left: 378px; top: 218px; --feature: var(--curry); }
  .label--chai    { left: 645px; top: 218px; --feature: var(--chai); }
  .label--oregano { left: 253px; top: 800px; --feature: var(--oregano); }
  .label--coffee  { left: 520px; top: 800px; --feature: var(--coffee); }
  .label--taco    { left: 778px; top: 800px; --feature: var(--taco); }

  .label__wave { position: absolute; inset: 0; width: 209px; height: 284px; }
  .label__wave path { fill: var(--feature); }

  .brand {
    position: absolute;
    top: 36px;
    left: 0;
    width: 100%;
    text-align: center;
    color: var(--ink);
    font-weight: 800;
    line-height: 1;
  }
  .brand__name { display: block; font-size: 27px; letter-spacing: -0.5px; }
  .brand__sub { display: block; font-size: 10px; letter-spacing: 5px; margin-top: 4px; }
  .slogan {
    position: absolute;
    top: 90px;
    left: 0;
    width: 100%;
    text-align: center;
    font-size: 6.5px;
    font-weight: 800;
    color: var(--ink);
    letter-spacing: 0.1px;
  }
  .slogan::after {
    content: "";
    display: block;
    width: 92px;
    height: 1px;
    margin: 2px auto 0;
    background: var(--ink);
  }

  .flavour {
    position: absolute;
    top: 188px;
    left: 0;
    width: 100%;
    text-align: center;
    color: var(--flavour-text);
    font-weight: 800;
    font-size: 25px;
    line-height: 32px;
    text-shadow: 1px 1px 2px rgba(0,0,0,0.35);
  }
  .flavour--single { top: 188px; }
</style>
</head>
<body>
<main class="sheet">

  <section class="label label--curry">
    <svg class="label__wave" viewBox="0 0 209 284" aria-hidden="true"><path d="M0 154 Q110 118 209 94 L209 284 L0 284 Z"/></svg>
    <div class="brand"><span class="brand__name">ZestoLane</span><span class="brand__sub">SPICES</span></div>
    <div class="slogan">WEIGHT LOSS SEASONINGS</div>
    <h2 class="flavour">MILD<br>CURRY</h2>
  </section>

  <section class="label label--chai">
    <svg class="label__wave" viewBox="0 0 209 284" aria-hidden="true"><path d="M0 154 Q110 118 209 94 L209 284 L0 284 Z"/></svg>
    <div class="brand"><span class="brand__name">ZestoLane</span><span class="brand__sub">SPICES</span></div>
    <div class="slogan">WEIGHT LOSS SEASONINGS</div>
    <h2 class="flavour">GOLDEN<br>CHAI</h2>
  </section>

  <section class="label label--oregano">
    <svg class="label__wave" viewBox="0 0 209 284" aria-hidden="true"><path d="M0 154 Q110 118 209 94 L209 284 L0 284 Z"/></svg>
    <div class="brand"><span class="brand__name">ZestoLane</span><span class="brand__sub">SPICES</span></div>
    <div class="slogan">WEIGHT LOSS SEASONINGS</div>
    <h2 class="flavour">GARLIC<br>OREGANO</h2>
  </section>

  <section class="label label--coffee">
    <svg class="label__wave" viewBox="0 0 209 284" aria-hidden="true"><path d="M0 154 Q110 118 209 94 L209 284 L0 284 Z"/></svg>
    <div class="brand"><span class="brand__name">ZestoLane</span><span class="brand__sub">SPICES</span></div>
    <div class="slogan">WEIGHT LOSS SEASONINGS</div>
    <h2 class="flavour">COFFEE<br>RUB</h2>
  </section>

  <section class="label label--taco">
    <svg class="label__wave" viewBox="0 0 209 284" aria-hidden="true"><path d="M0 154 Q110 118 209 94 L209 284 L0 284 Z"/></svg>
    <div class="brand"><span class="brand__name">ZestoLane</span><span class="brand__sub">SPICES</span></div>
    <div class="slogan">WEIGHT LOSS SEASONINGS</div>
    <h2 class="flavour flavour--single">TACO</h2>
  </section>

</main>
</body>
</html>
```